I need a DVD cover for a training package contained on a disc. There are four modules within the resource so I need these to be visible on the cover. They are:
Cultural Competence Healthcare Provision
Provision of Care to CALD Women having Babies in Australia
Cultural Considerations in Aged Care Provision
Cultural Competence in Mental Health

I have attached a cd cover with an image of a waratah. This is Corrowin Basin Health's logo so needs to appear on the front cover also.
The smaller logo with the waratah also needs to be on the front cover. Please note these are the only copies I could obtain so if the quality is too poor you may need to reproduce.

The following should appear on the back cover:
‘Pathways Beyond the Bedside’ is a collaborative achievement of the Multicultural Health Liaison Officers in Acute Care, Obstetrics, Aged Care and Mental Health under the guidance of the Director, Multicultural Health Service in Corrowin Basin Local Health District. Staff members from the specialist teams and community members graciously contributed to the production of podcasts and video clips.
Photography, video clips and technical support was provided by Gordon Velasky - E-learning Developer and Designer - Lumen Tutorworks.
This project was coordinated by Colette Brandt, Multicultural Health Liaison Officer (Acute Care, Tallowmere Ridge Clinical Hospital Network).

```html
<!DOCTYPE html>
<html lang="en">
<head>
<meta charset="utf-8">
<title>Pathways Beyond the Bedside – DVD Cover</title>
<link href="https://fonts.googleapis.com/css2?family=Montserrat:wght@400;500;700&family=Roboto:wght@400;700&display=swap" rel="stylesheet">
<style>
  :root {
    --page: #ffffff;
    --navy: #2b3b8f;
    --spine: #233a7c;
    --red: #e31c3d;
    --sky: #63c8ef;
    --sky-soft: #e9f6fc;
    --shadow: rgba(0,0,0,0.35);
    --text-dark: #111111;
  }
  * { margin: 0; padding: 0; box-sizing: border-box; }
  html, body { width: 1200px; height: 900px; overflow: hidden; background: var(--page); }
  body { position: relative; font-family: "Montserrat", sans-serif; }

  .dvd-cover {
    position: absolute; left: 105px; top: 94px; width: 991px; height: 668px;
    background: var(--page);
    border: 1px solid #d8d8d8;
    box-shadow: 4px 5px 6px var(--shadow);
    overflow: hidden;
  }

  /* back cover */
  .back-cover { position: absolute; left: 0; top: 0; width: 472px; height: 100%; }
  .photo-strip { position: absolute; left: 45px; top: 45px; display: flex; gap: 13px; }
  .photo-strip .photo { width: 89px; height: 67px; }
  .photo--doctors { background: linear-gradient(135deg, #e9e6e0, #b9b2a6); }
  .photo--parents { background: linear-gradient(135deg, #4a2e22, #c9b8a8); }
  .photo--elder { background: linear-gradient(135deg, #c47a3c, #8c7a5c); }
  .photo--thinking { background: linear-gradient(135deg, #2c4f7a, #d4a890); }

  .back-blurb {
    position: absolute; left: 45px; top: 184px; width: 375px;
    font-size: 11.4px; line-height: 15px; color: var(--navy); font-weight: 400;
  }
  .back-web {
    position: absolute; left: 45px; top: 618px;
    font-size: 11px; color: var(--red);
  }

  /* front cover */
  .front-cover {
    position: absolute; left: 518px; top: 0; width: 473px; height: 100%;
    background: linear-gradient(220deg, var(--sky) 0%, #bfe6f7 30%, var(--sky-soft) 60%, #ffffff 85%);
  }
  .brand-mark {
    position: absolute; right: 46px; top: 60px;
    display: flex; align-items: center; gap: 8px;
    font-size: 17px; font-weight: 500; color: var(--navy);
  }
  .brand-mark .brand-square { width: 14px; height: 14px; background: var(--navy); }
  .front-title {
    position: absolute; right: 46px; top: 184px;
    font-size: 18px; font-weight: 700; color: var(--red); text-align: right;
  }
  .module-list {
    position: absolute; right: 46px; top: 216px; list-style: none;
    text-align: right; color: var(--navy); font-size: 15px; line-height: 19px;
  }
  .module-list li { margin-bottom: 10px; }
  .producer {
    position: absolute; right: 46px; top: 586px; text-align: right;
    color: var(--navy); font-size: 11.5px; line-height: 15px;
  }
  .producer strong { display: block; font-weight: 700; }
  .producer .producer-label { display: block; margin-bottom: 3px; }

  /* decorative emblem area */
  .emblem-area {
    position: absolute; left: 250px; top: 366px; width: 506px; height: 290px;
    background: radial-gradient(ellipse at 50% 75%, rgba(227,28,61,0.22) 0%, rgba(227,28,61,0.10) 50%, rgba(227,28,61,0) 72%);
  }

  /* spine */
  .spine {
    position: absolute; left: 472px; top: 0; width: 46px; height: 100%;
    background: var(--spine); color: #ffffff;
  }
  .spine-title {
    position: absolute; left: 5px; top: 44px;
    writing-mode: vertical-rl; font-size: 12px; line-height: 16px;
  }
  .spine-title strong { font-weight: 700; font-size: 12.5px; }
  .spine-brand {
    position: absolute; left: 13px; top: 520px;
    writing-mode: vertical-rl; font-size: 10px; font-weight: 500;
    display: flex; align-items: center; gap: 5px;
  }
  .spine-brand .brand-square { width: 8px; height: 8px; background: #ffffff; }

  .caption {
    position: absolute; left: 0; width: 1200px; top: 778px; text-align: center;
    font-family: "Roboto", sans-serif; font-size: 13.5px; color: var(--text-dark);
  }
</style>
</head>
<body>
  <div class="dvd-cover">
    <section class="back-cover">
      <div class="photo-strip">
        <div class="photo photo--doctors" role="img" aria-label="Photo of three smiling clinicians"></div>
        <div class="photo photo--parents" role="img" aria-label="Photo of parents with a newborn"></div>
        <div class="photo photo--elder" role="img" aria-label="Photo of an elderly woman"></div>
        <div class="photo photo--thinking" role="img" aria-label="Photo of a pensive man"></div>
      </div>
      <p class="back-blurb">Pathways Beyond the Bedside’ was a collaborative achievement of the Multicultural Health Liaison Officers in Acute Care, Obstetrics, Aged Care and Mental Health under the guidance of the Director, Multicultural Health Service in Corrowin Basin Local Health District. Staff members from the specialist teams and community members graciously contributed to the production of podcasts and video clips. This project was coordinated by the Multicultural Health Service and Corrowin Basin Local Health District. Technical support was provided by Lumen Tutorworks.</p>
      <p class="back-web">www.corrowinhealth.example/multicultural_health</p>
    </section>

    <section class="front-cover">
      <div class="brand-mark"><span class="brand-square"></span>Corrowin Basin Health</div>
      <h1 class="front-title">Pathways Beyond the Bedside</h1>
      <ul class="module-list">
        <li>Culturally Competent Healthcare Provision</li>
        <li>Provision of Care to CALD Women<br>having Babies in Australia</li>
        <li>Cultural Considerations in Aged Care Provision</li>
        <li>Culture and Mental Health</li>
      </ul>
      <p class="producer"><span class="producer-label">Produced by</span><strong>Multicultural Health Service,</strong><strong>CB LHD</strong></p>
    </section>

    <div class="emblem-area" role="img" aria-label="Large brand flower emblem in red"></div>

    <aside class="spine">
      <p class="spine-title"><strong>Pathways Beyond the Bedside</strong><br>Produce by Multicultural Health Service, CB LHD</p>
      <div class="spine-brand"><span class="brand-square"></span>Corrowin Basin Health</div>
    </aside>
  </div>

  <p class="caption"><strong>Design 5:</strong> DVD Coversheet Revision</p>
</body>
</html>
```